Brochure for Coral Drift Voyages

A new brochure/A4 Flyer for our Coral Drift Voyages.
We have been operating a successful small business for 3 years in The Whisundays, QLD, Australia. The heart of the Great Barrier Reef.
We offer one-hour Coral Drift Voyages 3 times a day on our zero emissions electric boat for up to 8 guests.

Target Market(s)

All tourists visiting the Whitsundays. All ages and abilities

Industry/Entity Type

Tourism

Other font styles liked:
• Easy to read

Colors
0054AA
0677BA
7BADD7
CADEEF
E8F1F8
00AB8E
00BBA5
67D7C9
C6EFE9
E9F9F6

Requirements
Must have
• High impact font page. It's all about Bluewake Trips for one-hour.
Nice to have
• Bluewake Trips in top quarter/third of front page with a picture of a turtle
Should not have
• Not too much distraction on front page. More info on the back

```html
<!DOCTYPE html>
<html lang="en">
<head>
<meta charset="utf-8">
<title>Bluewake Trips – Tidewell Cruises Flyer</title>
<link rel="stylesheet" href="https://fonts.googleapis.com/css2?family=Bebas+Neue&family=Poppins:wght@400;500;600;700;800&display=swap">
<style>
:root{
  --stage:#dde9f4;
  --navy:#0b2148;
  --deep:#0a2a5e;
  --royal:#1340a8;
  --brand-blue:#0054aa;
  --yellow:#fff200;
  --red:#c4141a;
  --ink:#10182a;
  --white:#ffffff;
}
*{box-sizing:border-box;margin:0;padding:0}
html,body{width:1200px;height:957px;overflow:hidden}
body{background:var(--stage);font-family:"Poppins",sans-serif;position:relative}
.page{position:absolute;top:126px;width:500px;height:706px;overflow:hidden;box-shadow:0 6px 18px rgba(0,0,0,.18)}
.front{left:80px}
.back{left:620px;background:linear-gradient(180deg,#f2f2f3 0%,#e4e5e7 55%,#eeeeef 100%)}
.abs{position:absolute}

/* front */
.front-photo{inset:0;background:linear-gradient(180deg,#5c9fdd 0%,#a9cfee 24%,#45bfd8 40%,#1f86c7 50%,#0f5aa8 64%,#0a3c83 82%,#071e48 100%)}
.brand-front{left:0;right:0;top:38px;text-align:center}
.brand-name{font-weight:600;color:#1f2b46;font-size:30px;letter-spacing:1px;line-height:1}
.brand-sub{font-weight:600;color:#1f2b46;font-size:13px;letter-spacing:6px;margin-top:4px}
.title-word{font-family:"Bebas Neue",sans-serif;line-height:1;white-space:nowrap;transform-origin:left top}
.front-t1{left:86px;top:318px;font-size:106px;color:var(--yellow);transform:scaleY(1.95);text-shadow:0 2px 6px rgba(0,0,0,.25)}
.front-t2{left:86px;top:478px;font-size:104px;color:#1c8ad8;transform:scaleY(1.2)}
.badge{left:264px;top:502px;width:76px;height:76px;border-radius:50%;background:var(--red);border:3px dashed #ff6a6a;text-align:center;display:flex;flex-direction:column;justify-content:center;align-items:center}
.badge .lbl{font-size:7px;font-weight:700;letter-spacing:.5px;color:var(--yellow)}
.badge .num{font-family:"Bebas Neue",sans-serif;font-size:20px;color:var(--yellow);line-height:1}
.lede-front{left:98px;top:592px;width:200px;color:var(--white);font-size:13.4px;line-height:1.16}
.lede-front b{color:var(--yellow);font-weight:700}
.url-front{left:0;right:0;top:666px;text-align:center;color:var(--yellow);font-weight:700;font-size:14px;letter-spacing:3.6px}

/* back */
.back-title{left:76px;top:20px;font-size:67px;color:var(--royal);transform:scaleY(1.35)}
.meet{left:0;right:0;top:106px;text-align:center;font-size:8.4px;font-weight:500;color:var(--ink);line-height:1.3}
.pill-red{left:188px;top:134px;width:126px;height:17px;border-radius:9px;background:var(--red);color:var(--white);font-size:8.4px;font-weight:700;letter-spacing:1.2px;text-align:center;line-height:17px}
.rates{left:26px;top:175px;width:446px;height:111px;border:1px solid #7c8ab2;border-radius:12px}
.rates-head{left:0;right:0;top:-12px;text-align:center}
.rates-head span{background:#ececee;padding:0 6px;font-size:17px;letter-spacing:3.6px;color:var(--ink)}
.rates-head b{font-weight:800}
.divider{width:1px;background:#8b95b3}
.rate-title{font-size:10.4px;font-weight:700;color:var(--deep);white-space:nowrap}
.price{font-family:"Bebas Neue",sans-serif;color:var(--royal);font-size:30px;line-height:1;white-space:nowrap}
.price sup{font-size:13px;vertical-align:top;position:relative;top:2px}
.note{font-size:7.4px;color:var(--ink);line-height:1.2;white-space:nowrap}
.note.wrap{white-space:normal}
.pill-dark{height:14px;border-radius:7px;background:var(--navy);color:var(--white);font-size:7.2px;font-weight:600;line-height:14px;text-align:center}
.charter-head{left:26px;top:310px;font-size:13.6px;font-weight:800;color:var(--navy)}
.charter-head span{color:var(--brand-blue)}
.charter-copy{left:27px;top:334px;width:226px;font-size:7.2px;line-height:1.24;color:var(--ink)}
.perks{left:27px;top:400px;width:232px;list-style:none}
.perks li{position:relative;padding-left:14px;font-size:7.2px;line-height:1.24;color:var(--ink);margin-bottom:9px}
.perks svg{position:absolute;left:0;top:1px}
.challenge{left:27px;top:536px;font-size:10.4px;font-weight:700;color:var(--ink)}
.challenge span{color:var(--red)}
.snap{background:var(--white);padding:6px;box-shadow:0 3px 8px rgba(0,0,0,.3)}
.snap div{width:100%;height:100%}
.snap-1{left:292px;top:308px;width:122px;height:122px;transform:rotate(-4deg)}
.snap-1 div{background:linear-gradient(180deg,#5f7fae,#b9a898)}
.snap-2{left:318px;top:414px;width:132px;height:120px;transform:rotate(4deg)}
.snap-2 div{background:linear-gradient(180deg,#5d6f88,#3f82a6)}
.sea-band{left:0;right:0;top:560px;height:146px}
.brand-back{left:34px;top:630px}
.brand-back .brand-name{color:var(--white);font-size:26px}
.brand-back .brand-sub{color:var(--white);font-size:11px;letter-spacing:5px;padding-left:44px}
.phone{left:198px;top:636px;display:flex;align-items:center;gap:5px;color:var(--white);font-weight:700;font-size:24.5px;line-height:1}
.url-back{left:198px;top:670px;font-size:13px;letter-spacing:3.2px;color:var(--white)}
.url-back b{color:var(--yellow);font-weight:700}
</style>
</head>
<body>

<section class="page front">
  <div class="abs front-photo" role="img" aria-label="Photo: electric boat with guests near a tropical island, with a sea turtle and reef fish swimming underwater below"></div>

  <div class="abs brand-front">
    <div class="brand-name">Tidewell</div>
    <div class="brand-sub">CRUISES</div>
  </div>

  <h1>
    <span class="abs title-word front-t1">BLUEWAKE</span>
    <span class="abs title-word front-t2">TRIPS</span>
  </h1>

  <div class="abs badge">
    <svg width="14" height="10" viewBox="0 0 14 10"><circle cx="4" cy="3" r="2" fill="#fff200"/><circle cx="10" cy="3" r="2" fill="#fff200"/><path d="M0 10a4 4 0 0 1 8 0zM6 10a4 4 0 0 1 8 0z" fill="#fff200"/></svg>
    <span class="lbl">MAXIMUM</span>
    <span class="num">8 GUESTS</span>
  </div>

  <p class="abs lede-front">We offer <b>one-hour</b> Coral Drift Voyages <b>3 times a day</b> on our zero emissions electric boat</p>
  <p class="abs url-front">www.tidewellcruises.com.au</p>
</section>

<section class="page back">
  <h2 class="abs title-word back-title">BLUEWAKE TRIPS</h2>
  <p class="abs meet">Meet outside Marlin Bar &amp; Restaurant, Harbourside Marina<br>(North Complex) 10 minutes prior to departure.</p>
  <div class="abs pill-red">MAXIMUM 8 GUESTS</div>

  <div class="abs rates">
    <div class="abs rates-head"><span>TOURS <b>AVAILABLE DAILY</b></span></div>

    <div class="abs rate-title" style="left:12px;top:28px">Mimosa Morning Cruise</div>
    <div class="abs price" style="left:12px;top:42px"><sup>$</sup>85PP</div>
    <div class="abs note wrap" style="left:76px;top:45px;width:80px">Includes Mimosas/Orange Juice/Bubbles</div>
    <div class="abs pill-dark" style="left:12px;top:71px;width:42px">9.30am</div>

    <div class="abs divider" style="left:159px;top:24px;height:78px"></div>

    <div class="abs rate-title" style="left:172px;top:28px">One-Hour Coral Drift Voyages operate daily</div>
    <div class="abs price" style="left:174px;top:45px"><sup>$</sup>69PP</div>
    <div class="abs note" style="left:180px;top:77px">Adults (16+)</div>
    <div class="abs divider" style="left:238px;top:46px;height:40px"></div>
    <div class="abs price" style="left:246px;top:45px"><sup>$</sup>55PP</div>
    <div class="abs note" style="left:249px;top:77px">Child(1-15yo)</div>
    <div class="abs divider" style="left:312px;top:46px;height:40px"></div>
    <div class="abs price" style="left:322px;top:45px">INFANTS</div>
    <div class="abs note" style="left:342px;top:77px">FOC (0-1)</div>
    <div class="abs pill-dark" style="left:176px;top:89px;width:104px">At 11.00am and 12.30pm</div>
  </div>

  <h3 class="abs charter-head">PRIVATE <span>CHARTERS AVAILABLE</span></h3>
  <p class="abs charter-copy">Embark on an extraordinary and environmentally responsible journey by stepping aboard Airlie Beach's most unique tour. Join us for an intimate and serene adventure where sustainability meets luxury, creating memories that are as gentle on the environment as they are unforgettable.</p>

  <ul class="abs perks">
    <li><svg width="9" height="9" viewBox="0 0 9 9"><circle cx="4.5" cy="4.5" r="4.5" fill="#1340a8"/><path d="M2.3 4.6l1.5 1.4 2.9-3" stroke="#fff" stroke-width="1.1" fill="none"/></svg>With a maximum capacity of just 8 passengers, our charming vessel 'Marina Belle' stands out as the only electric boat in the Whitsundays.</li>
    <li><svg width="9" height="9" viewBox="0 0 9 9"><circle cx="4.5" cy="4.5" r="4.5" fill="#1340a8"/><path d="M2.3 4.6l1.5 1.4 2.9-3" stroke="#fff" stroke-width="1.1" fill="none"/></svg>Experience the magic of spotting turtles in eco-friendly luxury, gliding though calm waters with our whisper-quiet, fume-free electric boat.</li>
    <li><svg width="9" height="9" viewBox="0 0 9 9"><circle cx="4.5" cy="4.5" r="4.5" fill="#1340a8"/><path d="M2.3 4.6l1.5 1.4 2.9-3" stroke="#fff" stroke-width="1.1" fill="none"/></svg>Be on the lookout for the endangered loggerhead and green sea turtles. Immerse yourself in a serene journey as we tour through Turtle Bay, around Pigeon Island and the local foreshore, then back past the million-dollar yachts in the Harbourside Marina.</li>
  </ul>

  <p class="abs challenge">Can you beat our <span>'turtle count'</span> record?</p>

  <div class="abs snap snap-1"><div role="img" aria-label="Photo: guests relaxing aboard the boat under its canopy"></div></div>
  <div class="abs snap snap-2"><div role="img" aria-label="Photo: electric boat cruising in a calm bay"></div></div>

  <svg class="abs sea-band" viewBox="0 0 500 146" preserveAspectRatio="none" role="img" aria-label="Deep blue ocean band with a sea turtle photo at the surface">
    <defs><linearGradient id="seaGrad" x1="0" y1="0" x2="0" y2="1"><stop offset="0" stop-color="#1d3e78"/><stop offset="1" stop-color="#0a1f4a"/></linearGradient></defs>
    <path d="M0 8 L30 4 L60 12 L95 2 L130 10 L170 3 L210 11 L250 4 L290 10 L330 2 L370 9 L410 3 L450 10 L500 0 V146 H0 Z" fill="url(#seaGrad)"/>
  </svg>

  <div class="abs brand-back">
    <div class="brand-name">Tidewell</div>
    <div class="brand-sub">CRUISES</div>
  </div>

  <div class="abs phone">
    <svg width="18" height="18" viewBox="0 0 18 18"><circle cx="9" cy="9" r="9" fill="#fff200"/><path d="M6 4.5c.5-.3 1-.2 1.3.3l.8 1.5c.2.4.1.9-.2 1.1l-.6.5c.5 1.1 1.3 1.9 2.4 2.4l.5-.6c.3-.3.7-.4 1.1-.2l1.5.8c.5.3.6.8.3 1.3l-.5.8c-.4.6-1.1.9-1.8.6C8.4 12.1 6 9.7 5.1 7.3c-.3-.7 0-1.4.6-1.8z" fill="#0b2148"/></svg>
    0400 731 562
  </div>
  <p class="abs url-back">www.<b>tidewellcruises</b>.com.au</p>
</section>

</body>
</html>
```